Building company buisness cards

We are looking for a sharp modern new look for our business cards.We are a New Zealand based company that specialises in house and land packages.We have attached a photo of the current logo and would like to see if it can be improved somehow if needed.We are open to any colours but we have chosen Black and White at this stage. Feel free to change the font and make the logo smarter looking.Play with the colours and see what looks best.We want a card that looks so good know one will want to throw it away!

Target Market(s)

Building profesonals, home buyers

Industry/Entity Type

Building

Contact Information for Business Card

Derek Haskins
0274930268
derekh@stonerange.co.nz

Font styles to use
Serif
Sans Serif

Colors

Designer to choose colors to be used in the design.

Requirements
Must have
• Just the logo on one side and details on the other
• Clean simple looking card
Nice to have
• Round corners and detail like raised or spot UV
• Something that stands out
Should not have
• To title needed, Director etc

```html
<!DOCTYPE html>
<html lang="en">
<head>
<meta charset="utf-8">
<title>Stonerange Business Cards</title>
<link rel="stylesheet" href="https://fonts.googleapis.com/css2?family=Poppins:wght@400;500&display=swap">
<style>
  :root {
    --backdrop: #1c1d20;
    --card-top: #16171a;
    --card-bottom: #0b0b0d;
    --silver: #cfd0d2;
    --silver-soft: #a9abaf;
    --rule: rgba(255, 255, 255, 0.10);
    --icon-cut: #111214;
  }
  * { margin: 0; padding: 0; box-sizing: border-box; }
  html, body {
    width: 1200px;
    height: 900px;
    overflow: hidden;
    background: var(--backdrop);
  }
  .sheet {
    width: 1200px;
    height: 900px;
    display: flex;
    align-items: center;
    justify-content: center;
    gap: 60px;
  }
  .card {
    position: relative;
    width: 520px;
    height: 300px;
    border-radius: 30px;
    background: linear-gradient(160deg, var(--card-top), var(--card-bottom));
    box-shadow: 0 18px 40px rgba(0, 0, 0, 0.45);
    overflow: hidden;
  }

  /* Details side */
  .details__rule-v {
    position: absolute;
    left: 270px;
    top: 0;
    bottom: 0;
    width: 1px;
    background: var(--rule);
  }
  .details__rule-h {
    position: absolute;
    left: 230px;
    width: 80px;
    top: 150px;
    height: 1px;
    background: var(--rule);
  }
  .details__contact {
    position: absolute;
    right: 264px;
    top: 124px;
    text-align: right;
    font-family: "Poppins", sans-serif;
    font-size: 12px;
    line-height: 26px;
    color: var(--silver-soft);
    letter-spacing: 0.2px;
    padding-right: 14px;
  }
  .details__icons {
    position: absolute;
    left: 280px;
    top: 129px;
    display: flex;
    flex-direction: column;
    gap: 10px;
  }
  .details__icons svg { display: block; width: 16px; height: 16px; }
  .details__name {
    position: absolute;
    left: 318px;
    top: 152px;
    font-family: "Poppins", sans-serif;
    font-weight: 500;
    font-size: 17px;
    line-height: 22px;
    color: var(--silver);
    letter-spacing: 0.3px;
  }

  /* Logo side */
  .brand {
    position: absolute;
    inset: 0;
    display: flex;
    align-items: center;
    justify-content: center;
  }
  .brand__name {
    font-family: "Poppins", sans-serif;
    font-weight: 500;
    font-size: 40px;
    color: var(--silver);
    letter-spacing: 0.5px;
  }
</style>
</head>
<body>
  <main class="sheet">
    <section class="card card--details" aria-label="Contact side">
      <div class="details__rule-v"></div>
      <div class="details__rule-h"></div>
      <div class="details__contact">
        <p class="details__phone">0274930268</p>
        <p class="details__email">derekh@stonerange.co.nz</p>
      </div>
      <div class="details__icons">
        <svg viewBox="0 0 16 16" aria-label="Phone">
          <rect x="2" y="5" width="12" height="9" rx="2" fill="#a9abaf"/>
          <path d="M1 6 Q8 0 15 6" stroke="#a9abaf" stroke-width="2" fill="none"/>
          <circle cx="8" cy="9.5" r="2" fill="#111214"/>
        </svg>
        <svg viewBox="0 0 16 16" aria-label="Email">
          <rect x="1.5" y="3.5" width="13" height="9" rx="1" fill="#a9abaf"/>
          <path d="M1.5 4 L8 9 L14.5 4" stroke="#111214" stroke-width="1.2" fill="none"/>
        </svg>
      </div>
      <p class="details__name">Derek Haskins</p>
    </section>

    <section class="card card--brand" aria-label="Logo side">
      <div class="brand">
        <span class="brand__name">Stonerange</span>
      </div>
    </section>
  </main>
</body>
</html>
```